Applied environmental services company startup chasing a look

Small team of practical, technical and management-focused people in a business that can write the report, do the work written up in the report cost effectively. Vertical integration from design through to application. This business will be chasing opportunities where project management melds with technical application for clients needing forestry, environmental or natural resource management work done. We need a graphic and style for use in Microsoft Word and Powerpoint. A template including fonts, headings and styles would be great. Don't have a name yet, however I do like Verdant Ledge, Birchline Crest, Moorfield Holdings...

It Company

• I would like different shades of blue to be a part of the design.

```html
<!DOCTYPE html>
<html lang="en">
<head>
<meta charset="utf-8">
<title>Verdant Ledge – Title Slide</title>
<link href="https://fonts.googleapis.com/css2?family=Montserrat:wght@400;700&display=swap" rel="stylesheet">
<style>
  :root {
    --ocean-blue: #3589a8;
    --leaf-green: #4cbb82;
    --paper-white: #ffffff;
  }
  html, body {
    margin: 0;
    padding: 0;
    width: 1200px;
    height: 900px;
    overflow: hidden;
    background: var(--paper-white);
  }
  .slide {
    position: relative;
    width: 1200px;
    height: 900px;
    background: var(--ocean-blue);
    font-family: "Montserrat", Arial, sans-serif;
    overflow: hidden;
  }
  .corner-wave {
    position: absolute;
    left: 0;
    top: 0;
    width: 1200px;
    height: 900px;
  }
  .slide-title {
    position: absolute;
    left: 101px;
    top: 194px;
    margin: 0;
    font-size: 112px;
    line-height: 102px;
    font-weight: 700;
    color: var(--paper-white);
    letter-spacing: 0.5px;
  }
  .presenter-name {
    position: absolute;
    left: 102px;
    top: 520px;
    margin: 0;
    font-size: 47px;
    line-height: 56px;
    font-weight: 700;
    color: var(--leaf-green);
  }
  .presentation-date {
    position: absolute;
    left: 102px;
    top: 576px;
    margin: 0;
    font-size: 37px;
    line-height: 49px;
    font-weight: 400;
    color: var(--leaf-green);
  }
  .page-nav {
    position: absolute;
    left: 140px;
    top: 809px;
    width: 124px;
    height: 56px;
  }
  .brand {
    position: absolute;
    left: 892px;
    top: 757px;
    display: flex;
    align-items: center;
    gap: 20px;
  }
  .brand-dot {
    width: 66px;
    height: 66px;
    border-radius: 50%;
    background: var(--leaf-green);
  }
  .brand-name {
    margin: 0;
    font-size: 37px;
    line-height: 41px;
    font-weight: 700;
    color: var(--ocean-blue);
  }
</style>
</head>
<body>
  <main class="slide">
    <svg class="corner-wave" viewBox="0 0 1024 768" aria-hidden="true">
      <path fill="var(--leaf-green)" d="M585,768 C640,740 670,660 690,590 C710,520 760,495 820,505 C900,515 960,470 1000,410 C1015,380 1024,345 1024,330 L1024,768 Z"/>
      <path fill="var(--paper-white)" d="M680,768 C720,740 740,680 770,630 C800,590 840,575 900,590 C960,605 1000,600 1024,575 L1024,768 Z"/>
    </svg>

    <h1 class="slide-title">Presentation<br>Title Put Here</h1>
    <p class="presenter-name">John Doe</p>
    <p class="presentation-date">October 14, 2013</p>

    <svg class="page-nav" viewBox="0 0 124 56" aria-label="Slide 1">
      <polygon points="0,28 12,18 12,38" fill="var(--paper-white)"/>
      <circle cx="62" cy="28" r="28" fill="var(--paper-white)"/>
      <text x="62" y="36" text-anchor="middle" font-family="Montserrat, Arial, sans-serif" font-size="22" font-weight="700" fill="var(--ocean-blue)">1</text>
      <polygon points="124,28 112,18 112,38" fill="var(--paper-white)"/>
    </svg>

    <div class="brand">
      <span class="brand-dot"></span>
      <p class="brand-name">Verdant<br>Ledge</p>
    </div>
  </main>
</body>
</html>
```